Christmas Flyer

Hi,
We are needing a flyer that communicates a Christmas message for our cafe.
We'd like to advertise:
"To all of our loyal customers, if you are lucky enough to be working Christmas Day, we will be open and serving you FREE COFFEE from 6am - 10am.
Thank you for all your support over the last 12 months, we hope you have a very Merry Christmas, and have a happy and safe holidays from Harbour Lantern Kitchen"

I have included our logo, and one of our previous flyers.

You can also check out our instagram. Instagram @harbourlanternkitchen

Industry/Entity Type

Cafe

```html
<!DOCTYPE html>
<html lang="en">
<head>
<meta charset="utf-8">
<title>Harbour Lantern Kitchen – Christmas Flyer</title>
<link rel="stylesheet" href="https://fonts.googleapis.com/css2?family=Bangers&family=Oswald:wght@400;500;600&family=Indie+Flower&display=swap">
<style>
  :root {
    --page-bg: #e6e6e6;
    --red-bright: #e0333c;
    --red-mid: #b8151c;
    --red-deep: #5e0709;
    --band-light: rgba(90, 8, 12, 0.45);
    --band-dark: rgba(70, 4, 8, 0.78);
    --green: #1fcf6b;
    --green-dark: #0c8a3e;
    --white: #ffffff;
    --soft-white: #f3e4e4;
    --cup-rim: #f4f4f4;
    --coffee: #9a5a34;
  }
  * { margin: 0; padding: 0; box-sizing: border-box; }
  html, body { width: 1200px; height: 1000px; overflow: hidden; }
  body { background: var(--page-bg); position: relative; }

  .flyer {
    position: absolute; left: 275px; top: 30px; width: 650px; height: 930px;
    overflow: hidden;
    background:
      radial-gradient(ellipse 420px 260px at 70% 8%, rgba(255,120,130,0.35), transparent 70%),
      linear-gradient(180deg, var(--red-bright) 0%, var(--red-mid) 35%, #8e0b10 70%, var(--red-deep) 100%);
  }

  .headline {
    position: absolute; top: 62px; left: 0; width: 100%;
    text-align: center; white-space: nowrap;
    font-family: "Bangers", cursive; font-weight: 400;
    font-size: 94px; line-height: 1; letter-spacing: 0;
    color: var(--green);
    text-shadow: 0 3px 0 var(--green-dark);
    transform: scaleX(0.82);
    transform-origin: 50% 50%;
  }

  .intro-band {
    position: absolute; top: 162px; left: 0; width: 100%; height: 24px;
    background: var(--band-light);
    display: flex; align-items: center; justify-content: center;
    font-family: "Oswald", sans-serif; font-size: 14px; font-weight: 400;
    color: var(--white); white-space: nowrap;
  }

  .offer-band {
    position: absolute; top: 190px; left: 0; width: 100%; height: 63px;
    background: var(--band-dark);
    display: flex; align-items: center; justify-content: center;
    font-family: "Oswald", sans-serif; font-size: 52px; font-weight: 600;
    line-height: 1; color: var(--white); letter-spacing: 0.5px; white-space: nowrap;
  }
  .offer-band .joiner { font-weight: 400; margin: 0 12px; }
  .offer-band .colon { margin-right: 12px; }

  .brand-mark {
    position: absolute; top: 300px; left: 34px; width: 150px;
    display: flex; flex-direction: column; align-items: center; gap: 8px;
    font-family: "Oswald", sans-serif; font-weight: 500; font-size: 18px;
    line-height: 1.15; color: var(--white); text-align: center;
  }
  .brand-mark .dot {
    width: 46px; height: 46px; border-radius: 50%; background: var(--white);
  }

  .thanks {
    position: absolute; top: 282px; left: 190px; width: 430px;
    text-align: center;
    font-family: "Indie Flower", cursive; font-size: 18px; line-height: 21px;
    color: var(--white); letter-spacing: 0.5px;
  }

  .coffee-photo {
    position: absolute; top: 395px; left: 106px; width: 432px; height: 432px;
    border-radius: 50%;
    background: radial-gradient(circle at 50% 50%, var(--coffee) 0 34%, #cfcfcf 35%, var(--cup-rim) 40%, #ffffff 70%, #dadada 100%);
    box-shadow: 0 10px 30px rgba(0,0,0,0.45);
  }

  .address {
    position: absolute; top: 846px; left: 0; width: 100%; text-align: center;
    font-family: "Oswald", sans-serif; color: var(--white);
  }
  .address .street { font-size: 16px; font-weight: 400; }
  .address .note { font-size: 11px; font-style: italic; color: var(--soft-white); margin-top: 4px; }
</style>
</head>
<body>
  <main class="flyer">
    <h1 class="headline">MERRY CHRISTMAS</h1>

    <p class="intro-band">To all of our loyal customers, if you are lucky enough to be working Christmas Day, we will be open and serving you</p>

    <p class="offer-band"><span>FREE COFFEE</span><span class="colon">:</span><span>6am</span><span class="joiner">to</span><span>10am</span></p>

    <div class="brand-mark">
      <span class="dot"></span>
      <span class="brand-name">Harbour Lantern Kitchen</span>
    </div>

    <p class="thanks">Thank you for all your support over the last<br>12 months, we hope you have a very<br>Merry Christmas, and have a happy and safe<br>holidays from Harbour Lantern Kitchen</p>

    <div class="coffee-photo" role="img" aria-label="Photo from above of a latte in a white cup and saucer with a cinnamon stick, latte art of the cafe name"></div>

    <div class="address">
      <p class="street">14 Wharf Lane, Seabright, Queensland</p>
      <p class="note">Located next to the main carpark at Seabright General Hospital</p>
    </div>
  </main>
</body>
</html>
```